Brightwell Homes Guide Business card

I have had at the logo designed here and attached. The business compares off the plan apartments in Sydney and provides quick comparison for new home buyers e.g price, floor plans and location. I would like the complimentary colours used on the business card. I would like it be unique but also look professional. I also have a website to gain inspiration from www.brightwellhomesguide.com.au
Updates
Industry/Entity Type
Business
Contact Information for Business Card
Helen Vostrakis
Director of Business Development
e: helen.vostrakis@brightwellhomesguide.com.au
p: (02) 8143 7692
m: 0431 572 908
w: www.brightwellhomesguide.com.au
Look and feel
Each slider illustrates characteristics of the customer's brand and the style your logo design should communicate.

```html
<!DOCTYPE html>
<html lang="en">
<head>
<meta charset="utf-8">
<title>Brightwell Homes Guide – Business Card</title>
<link rel="stylesheet" href="https://fonts.googleapis.com/css2?family=Lato:wght@400;700;900&display=swap">
<style>
  :root {
    --page-bg: #e4e5e7;
    --card-white: #ffffff;
    --card-shade: #ececec;
    --brand-blue: #1b9ad6;
    --brand-blue-deep: #0f7fc0;
    --brand-blue-light: #3cb4ea;
    --brand-green: #74b72e;
    --text-grey: #5d6166;
    --text-dark: #3a3d41;
    --accent-red: #e2542a;
    --accent-orange: #f2a24a;
  }
  * { box-sizing: border-box; margin: 0; padding: 0; }
  html, body {
    width: 1200px;
    height: 964px;
    overflow: hidden;
    background: var(--page-bg);
    font-family: "Lato", sans-serif;
  }
  .sheet {
    width: 1200px;
    height: 964px;
    display: flex;
    flex-direction: column;
    align-items: center;
    justify-content: center;
    gap: 64px;
  }
  .card {
    width: 620px;
    height: 354px;
    border-radius: 18px;
    position: relative;
    overflow: hidden;
    box-shadow: 0 6px 18px rgba(0,0,0,0.18);
  }

  /* Back side */
  .card--back {
    background: linear-gradient(135deg, var(--brand-blue-light) 0%, var(--brand-blue) 55%, var(--brand-blue-deep) 100%);
  }

  /* Front side */
  .card--front {
    background: linear-gradient(180deg, var(--card-white) 0%, var(--card-white) 70%, var(--card-shade) 100%);
  }
  .brand {
    position: absolute;
    top: 66px;
    left: 0;
    right: 0;
    display: flex;
    align-items: center;
    justify-content: center;
    gap: 14px;
  }
  .brand__mark {
    width: 30px;
    height: 30px;
    background: var(--brand-green);
    border-radius: 3px;
  }
  .brand__name {
    font-size: 34px;
    font-weight: 700;
    color: var(--brand-green);
    letter-spacing: 0.2px;
  }
  .divider {
    position: absolute;
    left: 290px;
    top: 166px;
    width: 2px;
    height: 100px;
    background: linear-gradient(180deg, rgba(242,162,74,0) 0%, var(--accent-orange) 30%, var(--accent-red) 60%, rgba(226,84,42,0) 100%);
  }
  .person {
    position: absolute;
    left: 44px;
    top: 226px;
    width: 236px;
  }
  .person__name {
    font-size: 21px;
    font-weight: 900;
    color: var(--brand-blue);
  }
  .person__role {
    margin-top: 6px;
    font-size: 13px;
    color: var(--text-grey);
    white-space: nowrap;
  }
  .contacts {
    position: absolute;
    left: 306px;
    top: 170px;
    list-style: none;
    display: flex;
    flex-direction: column;
    gap: 14px;
  }
  .contacts__item {
    display: flex;
    align-items: center;
    gap: 9px;
    font-size: 11.5px;
    color: var(--text-dark);
    white-space: nowrap;
  }
  .contacts__icon {
    width: 20px;
    height: 20px;
    flex: none;
  }
</style>
</head>
<body>
  <main class="sheet">
    <section class="card card--back" aria-label="Business card back"></section>

    <section class="card card--front" aria-label="Business card front">
      <div class="brand">
        <span class="brand__mark"></span>
        <span class="brand__name">Brightwell Homes Guide</span>
      </div>

      <div class="divider"></div>

      <div class="person">
        <p class="person__name">Helen Vostrakis</p>
        <p class="person__role">Director of Business Development</p>
      </div>

      <ul class="contacts">
        <li class="contacts__item">
          <svg class="contacts__icon" viewBox="0 0 20 20" aria-hidden="true">
            <circle cx="10" cy="10" r="10" fill="var(--brand-blue)"/>
            <path d="M7 5.5c.5-.4 1.1-.3 1.4.2l.9 1.5c.3.5.2 1-.2 1.3l-.6.4c.4 1 1.2 1.9 2.2 2.4l.4-.6c.3-.4.9-.5 1.3-.2l1.5.9c.5.3.6.9.2 1.4l-.6.7c-.6.6-1.5.8-2.3.4-2.2-1-3.9-2.8-4.8-5-.3-.8-.1-1.7.6-2.3z" fill="#fff"/>
          </svg>
          <span>p: (02) 8143 7692 &nbsp;|&nbsp; m: 0431 572 908</span>
        </li>
        <li class="contacts__item">
          <svg class="contacts__icon" viewBox="0 0 20 20" aria-hidden="true">
            <circle cx="10" cy="10" r="10" fill="var(--brand-blue)"/>
            <rect x="5" y="6.5" width="10" height="7" rx="1" fill="#fff"/>
            <path d="M5.4 7l4.6 3.6L14.6 7" fill="none" stroke="var(--brand-blue)" stroke-width="1"/>
          </svg>
          <span>helen.vostrakis@brightwellhomesguide.com.au</span>
        </li>
        <li class="contacts__item">
          <svg class="contacts__icon" viewBox="0 0 20 20" aria-hidden="true">
            <circle cx="10" cy="10" r="10" fill="var(--brand-blue)"/>
            <circle cx="10" cy="10" r="5" fill="none" stroke="#fff" stroke-width="1.2"/>
            <ellipse cx="10" cy="10" rx="2.2" ry="5" fill="none" stroke="#fff" stroke-width="1"/>
            <line x1="5" y1="10" x2="15" y2="10" stroke="#fff" stroke-width="1"/>
          </svg>
          <span>www.brightwellhomesguide.com.au</span>
        </li>
      </ul>
    </section>
  </main>
</body>
</html>
```